WINE LABEL for Cobble-K Estate.

We require a wine bottle label for our Cobble-K Estate brand new to the market.
A sample "mock-up" layout of the front and back label is attached. The Cobble-K writing can be a logo type design with any font the designer chooses keeping in mind this will be used on Stationary, business cards and vehicles as well so could included some creative design as long as its clear to read the "Cobble-K" We require a pair of "crusty cowboy boots" as the main theme of the label but the designer could use flair here and design inside a circle or leave as set out.The main thing is they are rugged looking. The label can be framed if appropriate and the use of a parchment look or old western looking idea could be used. We would limit colors to 3 for printing purposes so the combination of colors is up to the designer as long as it stands out on the label visually. The rear label components is attached but can be set-out in any form the designer chooses. The use of the mountain outline at the base of the rear label may add a nice addition to this as its the view we see from our vineyard. Anything else please message me directly.

Target Market(s)

Boutique vineyard label that stands out from the normal.

Contact Information for Business Card

Set out using the designs from the label.

Font styles to use
Other font styles liked:
• Designer to use their selection

Requirements
Must have
• as set out on attached label Mock-up.
• A western theme for the label is preferred.
Should not have
• photos or more than 3 colours

```html
<!DOCTYPE html>
<html lang="en">
<head>
<meta charset="utf-8">
<title>Cobble-K Estate – Pinot Noir Label</title>
<link href="https://fonts.googleapis.com/css2?family=Rye&family=Lobster&family=Arimo:wght@400;700&display=swap" rel="stylesheet">
<style>
  :root {
    --page: #ffffff;
    --frame-gold: #d3a21a;
    --label-cream: #fbf7d4;
    --ink-gold: #c6a026;
    --ink-deep-gold: #b38a12;
    --ink-black: #1d1a14;
    --boot-dark: #4a2c18;
    --boot-mid: #8a5a34;
    --boot-light: #b88458;
  }
  html, body {
    margin: 0;
    padding: 0;
    width: 1024px;
    height: 1200px;
    overflow: hidden;
    background: var(--page);
  }
  .label {
    position: relative;
    width: 1024px;
    height: 1200px;
  }
  .label-frame {
    position: absolute;
    inset: 0;
  }
  .line {
    position: absolute;
    left: 0;
    width: 1024px;
    margin: 0;
    text-align: center;
    line-height: 1;
  }
  .brand-name {
    top: 205px;
    font-family: "Arimo", sans-serif;
    font-weight: 700;
    font-size: 64px;
    color: var(--ink-gold);
  }
  .boots-art {
    position: absolute;
    left: 310px;
    top: 318px;
    width: 380px;
    height: 395px;
    border-radius: 40% 45% 30% 30%;
    background: radial-gradient(ellipse at 45% 45%, var(--boot-light) 0%, var(--boot-mid) 45%, var(--boot-dark) 100%);
  }
  .est-year {
    position: absolute;
    top: 486px;
    line-height: 1;
    font-family: "Arimo", sans-serif;
    font-size: 30px;
    color: var(--ink-black);
  }
  .est-year--label { left: 232px; }
  .est-year--year { left: 700px; }
  .region {
    top: 736px;
    font-family: "Rye", serif;
    font-size: 60px;
    color: var(--ink-gold);
  }
  .subregion {
    top: 806px;
    font-family: "Arimo", sans-serif;
    font-weight: 700;
    font-size: 22px;
    color: var(--ink-black);
  }
  .vineyard {
    top: 852px;
    font-family: "Arimo", sans-serif;
    font-size: 30px;
    color: var(--ink-black);
  }
  .varietal {
    top: 900px;
    font-family: "Lobster", cursive;
    font-size: 80px;
    color: var(--ink-deep-gold);
  }
  .vintage {
    top: 1004px;
    font-family: "Arimo", sans-serif;
    font-size: 30px;
    color: var(--ink-black);
  }
  .origin {
    top: 1044px;
    font-family: "Arimo", sans-serif;
    font-size: 30px;
    color: var(--ink-black);
  }
</style>
</head>
<body>
  <main class="label">
    <svg class="label-frame" width="1024" height="1200" viewBox="0 0 1024 1200" aria-hidden="true">
      <ellipse cx="512" cy="600" rx="462" ry="568" fill="var(--label-cream)" stroke="var(--frame-gold)" stroke-width="30"/>
    </svg>

    <h1 class="line brand-name">Cobble-K Estate</h1>

    <div class="boots-art" role="img" aria-label="Illustration of a pair of worn, rugged brown leather cowboy boots with spurs"></div>

    <span class="est-year est-year--label">EST.</span>
    <span class="est-year est-year--year">2007</span>

    <p class="line region">WAITAKI VALLEY</p>
    <p class="line subregion">NORTH OTAGO</p>
    <p class="line vineyard">Single Vineyard</p>
    <p class="line varietal">Pinot Noir</p>
    <p class="line vintage">2016</p>
    <p class="line origin">New Zealand Wine</p>
  </main>
</body>
</html>
```